Professional Financial services company want to rebrand their stationary

We need stationary design for Veltor Group, its a company with 4 member companys that include Veltor Auditing, Veltor Financial Consultancy, Veltor Debt Collection and Veltor Real Estate.

We are based in dubai so the designers need to keep in mind that we use both english and arabic so leave a space for the arabic writing.

We recently redesigned our Logo and would like to redesign our stationary to go along with it.

You will find attached the logo, please keep it looking professional and use the logo as a guide for colors when designing.

Good luck to everyone

Industry/Entity Type

Finance And Accounting

Font styles to use
Sans Serif

Colors
0292cd
33a6d7
3276b5
0355a3
ffffff
dbdbdb

Requirements
Must have
• Letterhead
• Business card
• Envelope small and A4
Nice to have
• Professional
• Space for Arabic and english

```html
<!DOCTYPE html>
<html lang="en">
<head>
<meta charset="utf-8">
<title>Veltor Group Stationery</title>
<link href="https://fonts.googleapis.com/css2?family=Montserrat:wght@500;600&family=Roboto:wght@400;500;700&family=Noto+Sans+Arabic:wght@400;600&display=swap" rel="stylesheet">
<style>
  :root{
    --stage:#dbdbdb;
    --paper:#ffffff;
    --paper-soft:#f6f6f6;
    --brand:#0272c2;
    --brand-dark:#0355a3;
    --ink:#555a60;
    --rule:#b9bcbf;
    --label:#333;
  }
  *{box-sizing:border-box;margin:0;padding:0}
  html,body{width:1200px;height:517px;overflow:hidden;background:var(--stage)}
  body{position:relative;font-family:"Roboto",Arial,sans-serif;color:var(--ink)}
  .piece{position:absolute;background:var(--paper);box-shadow:0 1px 3px rgba(0,0,0,.18);overflow:hidden}
  .label{position:absolute;font-size:6.5px;color:var(--label);text-align:center;width:200px}
  .ar{font-family:"Noto Sans Arabic",Arial,sans-serif;direction:rtl}
  .wordmark{position:absolute;font-family:"Montserrat",Arial,sans-serif;font-weight:600;color:var(--brand);white-space:nowrap;letter-spacing:-.01em;line-height:1}
  .band{position:absolute;left:0;right:0;bottom:0;background:var(--brand);border-top:1.5px solid var(--rule)}

  /* business card */
  .card-front{left:47px;top:232px;width:197px;height:112px;text-align:center}
  .card-front .wordmark{left:0;right:0;top:22px;font-size:15px}
  .card-front .who{position:absolute;left:0;right:0;top:50px;display:flex;justify-content:center;gap:5px}
  .card-front .en{text-align:right;font-size:5px;line-height:1.35;padding-right:5px;border-right:.7px solid var(--rule)}
  .card-front .en .name{font-weight:700;color:var(--brand);font-size:7px}
  .card-front .arcol{text-align:right;font-size:5.2px;line-height:1.3}
  .card-front .arcol .name{font-weight:600;color:var(--brand);font-size:8px}
  .card-front .contact{position:absolute;left:0;right:0;top:90px;font-size:4.8px;line-height:1.4}
  .contact b{color:var(--brand)}
  .card-back{left:47px;top:365px;width:197px;height:112px;background:var(--brand);color:#fff;text-align:center}
  .card-back .wordmark{left:0;right:0;top:49px;color:#fff;font-size:12px}
  .card-back .members{position:absolute;left:0;right:0;top:83px;font-size:4.8px;line-height:1.45}
  .card-back .members strong{display:block;font-weight:700;margin-bottom:1px}

  /* letterhead */
  .letterhead{left:266px;top:76px;width:287px;height:402px}
  .letterhead .wordmark{left:25px;top:36px;font-size:10px}
  .letterhead .address{position:absolute;right:24px;top:34px;display:flex;gap:3px;font-size:4.3px;line-height:1.4}
  .letterhead .address .en{border-left:.6px solid var(--rule);padding-left:3px}
  .letterhead .body{position:absolute;left:25px;top:112px;width:240px;font-size:4.2px;line-height:1.72;color:var(--ink)}
  .letterhead .greeting{font-size:7px;margin-bottom:9px}
  .letterhead .body p{margin-bottom:7px;text-align:justify}
  .letterhead .sign{width:56px;height:20px;margin-top:6px;background:linear-gradient(90deg,rgba(2,114,194,.18),rgba(2,114,194,.05))}
  .letterhead .band{height:10px;display:flex;justify-content:center;align-items:center;gap:5px;font-size:4.2px;color:#fff}

  /* envelopes */
  .env-back{left:571px;top:186px;width:289px;height:131px}
  .env-back svg{position:absolute;left:0;top:0}
  .env-back .web{position:absolute;left:0;right:0;top:21px;text-align:center;color:#fff;font-size:4.5px}
  .env-front{left:571px;top:346px;width:290px;height:132px;background:linear-gradient(90deg,var(--paper),var(--paper-soft))}
  .env-front .wordmark{left:17px;top:25px;font-size:9px}
  .addr-block{position:absolute;font-size:4.3px;line-height:1.45}
  .env-front .addr-block{left:17px;top:46px}
  .env-front .band{height:10px}
  .env-a4{left:878px;top:35px;width:286px;height:443px;background:linear-gradient(90deg,var(--paper),var(--paper-soft));box-shadow:none;overflow:visible}
  .env-a4 .sheet{position:absolute;left:0;top:40px;right:0;bottom:0;background:inherit;box-shadow:0 1px 3px rgba(0,0,0,.18)}
  .env-a4 svg{position:absolute;left:0;top:0}
  .env-a4 .web{position:absolute;left:140px;top:16px;color:#fff;font-size:4.2px;transform:rotate(180deg)}
  .env-a4 .wordmark{left:22px;top:67px;font-size:9px}
  .env-a4 .addr-block{left:22px;top:90px}
  .env-a4 .band{height:11px}
</style>
</head>
<body>

<section class="piece card-front" aria-label="Business card, front">
  <div class="wordmark">VELTOR GROUP</div>
  <div class="who">
    <div class="en"><div class="name">OMAR HADDAD</div>CEO/FOUNDER<br>4120 Cedar Hollow Road<br>Marlow Bay, Westfield 20815</div>
    <div class="arcol ar"><div class="name">عمر حداد</div>مؤسس<br>4120 طريق سيدار<br>مارلو باي 20815</div>
  </div>
  <div class="contact"><b>P:</b> 555 210 4471 <b>C:</b> 555 318 7702 <b>F:</b> 555 604 2259<br><b>E:</b> info@veltorgroup.com <b>W:</b> www.veltorgroup.com</div>
</section>
<div class="label" style="left:45px;top:348px">Front Card</div>

<section class="piece card-back" aria-label="Business card, back">
  <div class="wordmark">VELTOR GROUP</div>
  <div class="members"><strong>MEMBER COMPANIES</strong>Veltor Auditing | Veltor Financial Consultancy<br>Veltor Debt Collection | Veltor Real Estate</div>
</section>
<div class="label" style="left:48px;top:485px">Back Card</div>

<section class="piece letterhead" aria-label="Letterhead">
  <div class="wordmark">VELTOR GROUP</div>
  <div class="address"><div class="ar">4120 طريق سيدار<br>مارلو باي 20815</div><div class="en">4120 Cedar Hollow Road<br>Marlow Bay, Westfield 20815</div></div>
  <div class="body">
    <div class="greeting">Dear Mr. Haddad,</div>
    <p>Lorem ipsum dolor sit amet, consectetur adipiscing elit. Donec orci purus, luctus vitae dignissim eu, iaculis sed purus. Vivamus faucibus, ipsum nec aliquet viverra, leo mauris condimentum ligula, sit amet sagittis enim ligula quis arcu. Nam egestas tortor id nisi porttitor mattis. In tortor ante, ultricies in suscipit a, tempus non massa. Vivamus et auctor mi. Fusce vel massa nulla. Phasellus nec eros mauris, et scelerisque orci.</p>
    <p>Donec malesuada orci vitae nulla accumsan porta a id massa. Quisque accumsan iaculis magna sit amet fringilla. Maecenas consequat, magna eget tincidunt semper, odio nibh rutrum mi, id feugiat ante nisi eu risus. Vestibulum nunc orci, rhoncus a placerat in, ultricies in mi. Cras mattis varius eros, vel fringilla nisi suscipit eget. Quisque scelerisque sagittis nulla at porttitor.</p>
    <p>Sed id augue vitae urna euismod commodo aliquet a quam. Pellentesque arcu velit, cursus et malesuada ut, consequat et diam. Nullam erat sem, rhoncus id ullamcorper vitae, rhoncus et arcu. In ultricies ultricies nulla, ut rutrum nisi iaculis at. Donec eu magna a metus ornare faucibus. Fusce aliquet faucibus ultricies. Morbi semper, est id tincidunt gravida, sem arcu adipiscing lacus, ac bibendum nulla leo eu purus.</p>
    <p>It is a long established fact that a reader will be distracted by the readable content of a page when looking at its layout. The point of using placeholder text is that it has a more-or-less normal distribution of letters, making it look like readable English.</p>
    <p>Sincerely,</p>
    <div class="sign" role="img" aria-label="Handwritten signature"></div>
  </div>
  <div class="band"><span>&#9742; 555 210 4471</span><span>555 318 7702</span><span>555 604 2259</span><span>&#9993; info@veltorgroup.com</span><span>www.veltorgroup.com</span></div>
</section>
<div class="label" style="left:310px;top:486px">Letter head</div>

<section class="piece env-back" aria-label="Envelope, back">
  <svg width="289" height="42" viewBox="0 0 289 42"><path d="M0 0H289V4Q286 24 270 32Q256 40 236 40H53Q33 40 19 32Q3 24 0 4Z" fill="var(--brand)"/></svg>
  <div class="web">www.veltorgroup.com</div>
</section>
<div class="label" style="left:616px;top:324px">Envelope Back</div>

<section class="piece env-front" aria-label="Envelope, front">
  <div class="wordmark">VELTOR GROUP</div>
  <div class="addr-block">4120 Cedar Hollow Road<br>Marlow Bay, Westfield 20815<br><span class="ar">4120 طريق سيدار<br>مارلو باي 20815</span></div>
  <div class="band"></div>
</section>
<div class="label" style="left:616px;top:485px">Envelope Front</div>

<section class="piece env-a4" aria-label="A4 envelope">
  <svg width="286" height="42" viewBox="0 0 286 42"><path d="M0 40L4 12Q6 0 18 0H268Q280 0 282 12L286 40Z" fill="var(--brand)"/></svg>
  <div class="sheet"></div>
  <div class="web">www.veltorgroup.com</div>
  <div class="wordmark">VELTOR GROUP</div>
  <div class="addr-block">4120 Cedar Hollow Road<br>Marlow Bay, Westfield 20815<br><span class="ar">4120 طريق سيدار<br>مارلو باي 20815</span></div>
  <div class="band"></div>
</section>
<div class="label" style="left:921px;top:485px">Envelope A4 Size</div>

</body>
</html>
```